Letterhead Design

We need a new Letterhead design for a 30 year old Electrical Company. We service domestic and commercial places. We have a logo recently made so to incorporate that. Using same colours or interested to see others added.
Would like to see a couple of options with all the info in letterhead, then another with info in a footnote down the bottom.

info needed to be added:

-Lic. No 48162
8/22-24 Larkin Rd, Tolvern 2087
W - brightcoilpower.com.au
T - (02) 9471 3825
M - 0427 593 168
E - info@brightcoilpower.com.au
ABN: 42 597 214 630

Electrical

```html
<!DOCTYPE html>
<html lang="en">
<head>
<meta charset="UTF-8">
<title>Brightcoil Power – Letterhead</title>
<link href="https://fonts.googleapis.com/css2?family=Montserrat:wght@400;500;600&display=swap" rel="stylesheet">
<style>
  :root {
    --navy: #1f3550;
    --orange: #f7941d;
    --grey: #6d6e71;
    --dark: #231f20;
    --paper: #ffffff;
  }
  * { margin: 0; padding: 0; box-sizing: border-box; }
  html, body {
    width: 849px;
    height: 1200px;
    overflow: hidden;
    background: var(--paper);
  }
  .letterhead {
    position: relative;
    width: 849px;
    height: 1200px;
    background: var(--paper);
    font-family: "Montserrat", Arial, sans-serif;
  }
  .brand {
    position: absolute;
    left: 105px;
    top: 118px;
    display: flex;
    align-items: center;
    gap: 14px;
  }
  .brand-mark {
    width: 34px;
    height: 34px;
    background: var(--navy);
  }
  .brand-name {
    font-size: 40px;
    font-weight: 600;
    color: var(--navy);
    letter-spacing: 0.5px;
    line-height: 1;
  }
  .contact {
    position: absolute;
    left: 105px;
    top: 436px;
    list-style: none;
    font-size: 12px;
    color: var(--grey);
    line-height: 22.5px;
  }
  .contact .label {
    color: var(--orange);
    font-weight: 600;
    margin-right: 6px;
  }
  .contact .value-strong {
    color: var(--dark);
    font-weight: 600;
  }
  .contact .web {
    color: var(--orange);
  }
  .contact .small {
    font-size: 10px;
  }
  .footer-band {
    position: absolute;
    left: 0;
    bottom: 0;
    width: 849px;
    height: 45px;
    background: var(--orange);
  }
</style>
</head>
<body>
  <div class="letterhead">
    <header class="brand">
      <span class="brand-mark"></span>
      <span class="brand-name">Brightcoil Power</span>
    </header>

    <ul class="contact">
      <li class="small">Lic. No 48162</li>
      <li>8/22-24 Larkin Rd, Tolvern 2087</li>
      <li><span class="label">T</span><span class="value-strong">(02) 9471 3825</span></li>
      <li><span class="label">M</span><span class="value-strong">0427 593 168</span></li>
      <li><span class="label">E</span><span class="value-strong">info@brightcoilpower.com.au</span></li>
      <li class="web">www.brightcoilpower.com.au</li>
      <li class="small">ABN: 42 597 214 630</li>
    </ul>

    <div class="footer-band"></div>
  </div>
</body>
</html>
```